Wellness, Purpose, and the Quiet Path Research Program Website

Overview: This website will serve a new research program (Wellness, Purpose, and the Quiet Path) at the Thornbury University School of Medicine. I want a clean, intuitive design that has a navigation bar, but uses icons/graphic buttons to link to the main pages. In an attached Word document, I have provided a basic information architecture for the site, understanding that this project would just generate graphics and code for the 3 pages. I highlighted the 3 pages I'd like designed.
Target market: People who want to participate in our research, or contribute grant funding to specific projects.
Number of page: The design project focuses on 3 pages, but the site must accommodate 6 pages with top-level links. See attached Word doc.
Logo and website header: Please integrate our logo in the header. I've uploaded it as a png file--both with the name of the website and with just the logo image. I imaging the logo would look great in a banner set against an image of a mountain. The two main design themes I want to see included are nature and healthcare.
Text content: I have not yet provided text. Use some dummy text.
Technical Specifications:
- Build using WordPress. We will host this site ourselves on HostBarrow using WordPress.
- The design package must be coded.
- The template must be responsive to different platforms (e.g., computer, mobile phone, Zelvo).
Thank you! I look forward to seeing your designs.
- Ned

```html
<!DOCTYPE html>
<html lang="en">
<head>
<meta charset="utf-8">
<title>Wellness, Purpose, and the Quiet Path Research Program</title>
<link href="https://fonts.googleapis.com/css2?family=Rubik:wght@400;500;700&family=Montserrat:wght@400;500;600;700&display=swap" rel="stylesheet">
<style>
:root{
  --green:#3f8f3b;
  --green-light:#57a843;
  --green-deep:#2f6e2b;
  --blue:#1d5c9b;
  --blue-deep:#144a80;
  --ink:#1c1c1c;
  --text:#4a4a4a;
  --black:#141414;
  --line:#cfcfcf;
  --white:#fff;
}
*{box-sizing:border-box;margin:0;padding:0}
html,body{width:1200px;height:4644px;overflow:hidden}
body{position:relative;background:var(--white);font-family:"Montserrat",sans-serif;color:var(--text)}
.abs{position:absolute}
a{color:inherit;text-decoration:none}

/* header */
.site-header{position:absolute;left:0;top:0;width:1200px;height:92px;background:var(--black)}
.brand{position:absolute;left:112px;top:28px;display:flex;align-items:center;gap:10px;color:var(--green-light);font-family:"Montserrat",sans-serif;font-weight:700;font-size:17px}
.brand i{width:22px;height:22px;border-radius:50%;background:var(--green-light);display:block}
.main-nav{position:absolute;left:343px;top:34px;display:flex;gap:40px;font-size:14px;color:#fff;font-weight:500}
.main-nav .active{color:var(--green-light)}
.btn{display:inline-flex;align-items:center;gap:14px;background:var(--green);color:#fff;border-radius:22px;font-weight:600;font-size:13px;padding:0 8px 0 18px;height:40px;box-shadow:0 3px 8px rgba(0,0,0,.18)}
.btn .dot{width:24px;height:24px;border-radius:50%;background:#fff;display:flex;align-items:center;justify-content:center}
.btn-contact{position:absolute;left:960px;top:24px;height:42px;padding:0 26px;font-size:13px;border:2px solid var(--green-light)}

/* hero */
.hero-photo{position:absolute;left:0;top:92px;width:1200px;height:620px;background:linear-gradient(180deg,#7fb4df 0%,#8db86a 28%,#4d7d2e 55%,#6f9db8 78%,#4f7b3a 100%)}
.hero-title{position:absolute;left:112px;top:274px;color:#fff;font-family:"Rubik",sans-serif;font-weight:700;font-size:29px;text-shadow:0 2px 6px rgba(0,0,0,.45)}
.hero-sub{position:absolute;left:112px;top:310px;color:#fff;font-family:"Rubik",sans-serif;font-weight:500;font-size:22px;text-shadow:0 2px 6px rgba(0,0,0,.45)}
.hero-btn{position:absolute;left:112px;top:360px}
.arrow-circle{position:absolute;top:305px;width:58px;height:58px;border-radius:50%;background:rgba(20,60,110,.75);border:2px solid rgba(255,255,255,.6);display:flex;align-items:center;justify-content:center}

/* section headings */
.section-title{position:absolute;left:0;width:1200px;display:flex;justify-content:center;align-items:center;gap:22px;font-family:"Rubik",sans-serif;font-size:28px;font-weight:500;color:var(--ink)}
.section-title .rule{width:124px;height:2px;background:var(--green)}
.section-title .accent{color:var(--blue);font-weight:400}
.section-title.light{color:#fff}
.section-title.light .rule{background:#fff;width:66px}

/* about */
.about-mark{position:absolute;left:150px;top:790px;width:400px;height:370px;display:flex;align-items:center;justify-content:center;gap:16px;font-family:"Montserrat",sans-serif;font-weight:700;font-size:34px;color:var(--blue)}
.about-mark i{width:46px;height:46px;border-radius:50%;background:var(--green);display:block}
.about-title{position:absolute;left:632px;top:808px;font-family:"Rubik",sans-serif;font-size:28px;font-weight:500;color:var(--ink);display:flex;align-items:center;gap:16px}
.about-title .accent{color:var(--blue);font-weight:400}
.about-title .rule{width:124px;height:2px;background:var(--green)}
.about-copy{position:absolute;left:632px;top:852px;width:408px;font-size:13.5px;line-height:22px}
.about-copy p+p{margin-top:10px}
.about-btn{position:absolute;left:630px;top:1103px}
.divider{position:absolute;left:111px;top:1240px;width:978px;height:1px;background:var(--line)}
.divider-knob{position:absolute;left:582px;top:1223px;width:36px;height:36px;border-radius:50%;background:var(--green);display:flex;align-items:center;justify-content:center;box-shadow:0 2px 6px rgba(0,0,0,.2)}

.vision-copy{position:absolute;left:140px;top:1398px;width:920px;text-align:center;font-size:13.5px;line-height:22px}

/* people */
.people-band{position:absolute;left:0;top:1530px;width:1200px;height:670px}
.person{position:absolute;top:1686px;width:230px;height:299px;background:#fff;border-radius:3px;overflow:hidden;text-align:center}
.person .photo{height:242px;background:linear-gradient(180deg,#c9b9a4,#8d7a66)}
.person h4{font-size:13.5px;font-weight:500;color:var(--ink);margin-top:12px}
.person span{display:block;font-size:12px;margin-top:2px}
.people-btn{position:absolute;left:529px;top:2020px}

/* research */
.project{position:absolute;background:#fff;border-radius:6px;box-shadow:0 4px 16px rgba(0,0,0,.15);text-align:center;padding:0 12px}
.project h5{font-weight:600;color:var(--ink)}
.project p{color:#777}
.project.side{top:2368px;width:306px;height:212px;padding-top:32px}
.project.side h5{font-size:11.5px;line-height:15px}
.project.side p{font-size:8.5px;line-height:15px;margin-top:10px}
.project.main{left:393px;top:2330px;width:414px;height:285px;padding:34px 20px 0}
.project.main h5{font-size:15.5px;line-height:21px}
.project.main p{font-size:13px;line-height:21px;margin-top:12px}
.dots{position:absolute;left:576px;top:2660px;display:flex;gap:4px}
.dots i{width:9px;height:9px;border-radius:50%;border:1.5px solid var(--blue);display:block}
.dots i.on{background:var(--blue)}

/* faq */
.faq-band{position:absolute;left:0;top:2740px;width:1200px;height:745px}
.faq-item{position:absolute;left:158px;width:912px;border-bottom:1px solid rgba(255,255,255,.6);color:#fff}
.faq-item h6{font-size:16.5px;font-weight:600;padding-left:36px;position:relative}
.faq-item h6::before{content:"+";position:absolute;left:0;top:-3px;font-size:22px;font-weight:500}
.faq-item.open h6::before{content:"–"}
.faq-item p{padding-left:36px;font-size:12.5px;line-height:21px;margin-top:10px}
.faq-btn{position:absolute;left:529px;top:3310px;background:#fff;color:var(--green)}
.faq-btn .dot{background:var(--green)}

/* contact */
.contact-copy{position:absolute;left:260px;top:3602px;width:680px;text-align:center;font-size:13.5px;line-height:20px}
.field{position:absolute;border:1px solid #c8c8c8;display:flex;align-items:center;gap:14px;padding-left:16px;font-size:13px;color:#777}
.field.tall{align-items:flex-start;padding-top:22px}
.submit-btn{position:absolute;left:529px;top:3975px}

/* footer */
.footer-band{position:absolute;left:0;top:4080px;width:1200px;height:564px}
.footer-brand{position:absolute;left:160px;top:4350px;display:flex;align-items:center;gap:12px;font-weight:700;font-size:26px;color:var(--green-light)}
.footer-brand i{width:30px;height:30px;border-radius:50%;background:var(--blue);display:block}
.footer-col{position:absolute;top:4296px;color:#fff}
.footer-col h3{font-family:"Rubik",sans-serif;font-weight:500;font-size:21px;display:inline-block;padding-bottom:4px;border-bottom:2px solid var(--green-light)}
.footer-col ul{list-style:none;margin-top:14px;font-size:13px;line-height:26px}
.contact-row{position:absolute;left:768px;display:flex;gap:22px;color:#fff;font-size:13px;line-height:20px}
.contact-row svg{flex:none;margin-top:2px}
.to-top{position:absolute;left:1102px;top:4500px;width:50px;height:50px;border-radius:50%;background:var(--green);display:flex;align-items:center;justify-content:center}
.footer-rule{position:absolute;left:106px;top:4560px;width:984px;height:1px;background:#444}
.copyright{position:absolute;left:106px;top:4585px;color:#fff;font-size:12.5px;font-weight:500}
.legal-links{position:absolute;left:900px;top:4585px;color:#fff;font-size:12.5px;font-weight:500;display:flex;gap:18px}
</style>
</head>
<body>

<header class="site-header">
  <a class="brand" href="#"><i></i>Quiet Path</a>
  <nav class="main-nav">
    <a class="active" href="#">Home</a><a href="#">About Us</a><a href="#">Vision Statement</a><a href="#">People</a><a href="#">Projects</a><a href="#">FAQs</a>
  </nav>
  <a class="btn btn-contact" href="#">Contact Us</a>
</header>

<div class="hero-photo" role="img" aria-label="Mountain river flowing through a pine forest valley"></div>
<svg class="abs" style="left:0;top:560px" width="1200" height="160" viewBox="0 0 1200 160">
  <path d="M0 62 C240 160 640 150 1200 40 L1200 160 L0 160 Z" fill="#2f6e2b"/>
  <path d="M0 86 C260 172 660 160 1200 52 L1200 160 L0 160 Z" fill="#fff"/>
</svg>
<h1 class="hero-title">Wellness, Purpose, and the Quiet Path</h1>
<p class="hero-sub">The Research Program</p>
<a class="btn hero-btn" href="#">Get Started <span class="dot"><svg width="10" height="10" viewBox="0 0 10 10"><path d="M3 1l4 4-4 4" stroke="#3f8f3b" stroke-width="1.8" fill="none"/></svg></span></a>
<div class="arrow-circle" style="left:26px"><svg width="14" height="14" viewBox="0 0 14 14"><path d="M9 2L4 7l5 5" stroke="#fff" stroke-width="2" fill="none"/></svg></div>
<div class="arrow-circle" style="left:1114px"><svg width="14" height="14" viewBox="0 0 14 14"><path d="M5 2l5 5-5 5" stroke="#fff" stroke-width="2" fill="none"/></svg></div>

<section>
  <div class="about-mark"><i></i>Quiet Path</div>
  <h2 class="about-title">About <span class="accent">Us</span><span class="rule"></span></h2>
  <div class="about-copy">
    <p>Perspiciatis unde omnis iste natus error sit voluptatem accusantium doloremque laudantiu eaqueillo inventore veritatis et quasi architecto.</p>
    <p>Doloremque laudantium, totam rem aperiam, eaque ipsa quae ab illo inventore veritatis et quasi architecto beatae vitae dicta sunt explicabo. Nemo enim ipsam voluptatem quia voluptas sit aspernatur aut odit aut fugit, sed quia consequuntur magni dolores eos qui ratione voluptatem sequi nesciunt. Neque porro quisquam est, qui dolorem ipsum quia dolor sit amet, consectetur.</p>
  </div>
  <a class="btn about-btn" href="#">Learn More <span class="dot"><svg width="10" height="10" viewBox="0 0 10 10"><path d="M3 1l4 4-4 4" stroke="#3f8f3b" stroke-width="1.8" fill="none"/></svg></span></a>
  <div class="divider"></div>
  <div class="divider-knob"><svg width="14" height="14" viewBox="0 0 14 14"><path d="M2 5l5 5 5-5" stroke="#fff" stroke-width="2" fill="none"/></svg></div>
</section>

<section>
  <h2 class="section-title" style="top:1338px"><span class="rule"></span><span>Vision <span class="accent">Satement</span></span><span class="rule"></span></h2>
  <p class="vision-copy">Doloremque laudantium, totam rem aperiam, eaque ipsa quae ab illo inventore veritatis et quasi architecto beatae vitae dicta sunt explicabo. Nemo enim ipsam voluptatem quia voluptas sit aspernatur aut odit aut fugit, sed quia consequuntur magni dolores eos qui ratione voluptatem sequi nesciunt. Neque porro quisquam est, qui dolorem ipsum quia dolor sit amet, consectetur.</p>
</section>

<section>
  <svg class="people-band" viewBox="0 0 1200 670" role="img" aria-label="Misty blue forest backdrop">
    <defs><linearGradient id="pb" x1="0" y1="0" x2="0" y2="1"><stop offset="0" stop-color="#1d5c9b"/><stop offset=".5" stop-color="#2b6aa6"/><stop offset="1" stop-color="#1a5591"/></linearGradient></defs>
    <path d="M0 0 C400 40 800 40 1200 8 L1200 620 C800 650 400 650 0 660 Z" fill="url(#pb)"/>
  </svg>
  <h2 class="section-title light" style="top:1620px"><span class="rule"></span><span>People</span><span class="rule"></span></h2>
  <div class="person" style="left:112px"><div class="photo" role="img" aria-label="Portrait of a smiling man with a backpack"></div><h4>Orin Vale</h4><span>Fistenatus Earrorsit</span></div>
  <div class="person" style="left:360px"><div class="photo" role="img" aria-label="Portrait of a smiling woman seated" style="background:linear-gradient(180deg,#e5e0d8,#a99b8c)"></div><h4>Mira T Holloway</h4><span>Fistenatus Earrorsit</span></div>
  <div class="person" style="left:608px"><div class="photo" role="img" aria-label="Portrait of a woman in a dark sweater" style="background:linear-gradient(180deg,#ececec,#3a3a3a)"></div><h4>Tessa L Marr</h4><span>Fistenatus Earrorsit</span></div>
  <div class="person" style="left:856px"><div class="photo" role="img" aria-label="Portrait of a man sitting by a railing" style="background:linear-gradient(180deg,#c0756a,#6d8fae)"></div><h4>Jonah P Kettle</h4><span>Fistenatus Earrorsit</span></div>
  <a class="btn people-btn" href="#">Learn More <span class="dot"><svg width="10" height="10" viewBox="0 0 10 10"><path d="M3 1l4 4-4 4" stroke="#3f8f3b" stroke-width="1.8" fill="none"/></svg></span></a>
</section>

<section>
  <h2 class="section-title" style="top:2256px"><span class="rule" style="width:124px"></span><span>Research <span class="accent">Projects</span></span><span class="rule"></span></h2>
  <article class="project side" style="left:66px"><h5>Kosolo remque lauda ntium totam rem aperiam eaque ipsaquae abillo inventore.</h5><p>Doloremque laudantium, totam rem aperiam, eaque ipsa quae ab illo inventore veritatis et quasi architecto beatae vitae dicta sunt explicabo. Nemo enim ipsam voluptatem quia voluptas sit aspernatur aut odit aut fugit, sed quia consequuntur magni dolores eos qui ratione voluptatem sequi nesciunt. Neque porro quisquam est, qui dolorem ipsum quia dolor sit amet, consectetur.</p></article>
  <article class="project main"><h5>Kosolo remque lauda ntium totam rem aperiam eaque ipsaquae abillo inventore.</h5><p>Doloremque laudantium, totam rem aperiam, eaque ipsa quae ab illo inventore veritatis et quasi architecto beatae vitae dicta sunt explicabo. Nemo enim ipsam voluptatem quia voluptas sit aspernatur aut odit aut fugit, sed quia consequuntur magni dolores eos qui ratione voluptatem sequi nesciunt. Neque porro quisquam est, qui dolorem ipsum quia dolor sit amet, consectetur.</p></article>
  <article class="project side" style="left:828px"><h5>Kosolo remque lauda ntium totam rem aperiam eaque ipsaquae abillo inventore.</h5><p>Doloremque laudantium, totam rem aperiam, eaque ipsa quae ab illo inventore veritatis et quasi architecto beatae vitae dicta sunt explicabo. Nemo enim ipsam voluptatem quia voluptas sit aspernatur aut odit aut fugit, sed quia consequuntur magni dolores eos qui ratione voluptatem sequi nesciunt. Neque porro quisquam est, qui dolorem ipsum quia dolor sit amet, consectetur.</p></article>
  <div class="dots"><i class="on"></i><i></i><i></i><i></i></div>
</section>

<section>
  <svg class="faq-band" viewBox="0 0 1200 745" role="img" aria-label="Green forested mountain valley backdrop">
    <defs><linearGradient id="fb" x1="0" y1="0" x2="0" y2="1"><stop offset="0" stop-color="#3d8a36"/><stop offset=".5" stop-color="#4f9a3f"/><stop offset="1" stop-color="#2f7a2c"/></linearGradient></defs>
    <path d="M0 0 C400 40 800 40 1200 14 L1200 725 C800 690 400 700 0 740 Z" fill="url(#fb)"/>
  </svg>
  <h2 class="section-title light" style="top:2856px"><span class="rule" style="width:124px"></span><span>FAQ's</span><span class="rule" style="width:124px"></span></h2>
  <div class="faq-item" style="top:2920px;height:38px"><h6>What makes this project unique?</h6></div>
  <div class="faq-item" style="top:2992px;height:38px"><h6>Does this project assume that the impact of religion is always positive?</h6></div>
  <div class="faq-item open" style="top:3065px;height:148px"><h6>Will Thornbury U faculty lead all projects?</h6><p>Doloremque laudantium, totam rem aperiam, eaque ipsa quae ab illo inventore veritatis et quasi architecto beatae vitae dicta sunt explicabo. Nemo enim ipsam voluptatem quia voluptas sit aspernatur aut odit aut fugit, sed quia consequuntur magni dolores eos qui ratione voluptatem sequi nesciunt. Neque porro quisquam est, qui dolorem ipsum quia dolor sit amet, consectetur. Iaiste natus error sit voluptatem accusantium doloremque laudantium, totam rem aperiam, eaque ipsa quae ab illo inventore veritatis et quasi architecto beatae vitae dicta sunt explicabo. Nemo enim ipsam voluptatem quia volu.</p></div>
  <div class="faq-item" style="top:3248px;height:38px"><h6>How can I collaborate?</h6></div>
  <a class="btn faq-btn" href="#">View More <span class="dot"><svg width="10" height="10" viewBox="0 0 10 10"><path d="M3 1l4 4-4 4" stroke="#fff" stroke-width="1.8" fill="none"/></svg></span></a>
</section>

<section>
  <h2 class="section-title" style="top:3550px"><span class="rule"></span><span>Contact <span class="accent">Us</span></span><span class="rule"></span></h2>
  <p class="contact-copy">Perspiciatis unde omnis iste natus error sit voluptatem accusantium doloremque laudantiu eaqueillo inventore veritatis et quasi architecto.</p>
  <div class="field" style="left:228px;top:3666px;width:357px;height:56px"><svg width="14" height="14" viewBox="0 0 14 14"><circle cx="7" cy="4" r="3.2" fill="#3f8f3b"/><path d="M1 14c0-4 3-6 6-6s6 2 6 6z" fill="#3f8f3b"/></svg>First Name</div>
  <div class="field" style="left:613px;top:3666px;width:356px;height:56px"><svg width="14" height="14" viewBox="0 0 14 14"><circle cx="7" cy="4" r="3.2" fill="#3f8f3b"/><path d="M1 14c0-4 3-6 6-6s6 2 6 6z" fill="#3f8f3b"/></svg>First Name</div>
  <div class="field" style="left:228px;top:3739px;width:357px;height:56px"><svg width="14" height="11" viewBox="0 0 14 11"><rect width="14" height="11" rx="1" fill="#3f8f3b"/><path d="M1 1l6 5 6-5" stroke="#fff" stroke-width="1.3" fill="none"/></svg>Email</div>
  <div class="field" style="left:613px;top:3739px;width:356px;height:56px"><svg width="14" height="14" viewBox="0 0 14 14"><path d="M3 1l2.5 3-1.5 2c1 2 2 3 4 4l2-1.5 3 2.5-1.5 2.5C6 13 1 8 .5 3z" fill="#3f8f3b"/></svg>Phone</div>
  <div class="field tall" style="left:228px;top:3811px;width:741px;height:137px"><svg width="16" height="13" viewBox="0 0 16 13"><rect x=".7" y=".7" width="10" height="7" rx="2" fill="none" stroke="#8bbd7f" stroke-width="1.3"/><rect x="5" y="4.5" width="10" height="7" rx="2" fill="none" stroke="#8bbd7f" stroke-width="1.3"/></svg>Message</div>
  <a class="btn submit-btn" href="#" style="padding-right:8px;gap:60px">Submit <span class="dot"><svg width="10" height="10" viewBox="0 0 10 10"><path d="M3 1l4 4-4 4" stroke="#3f8f3b" stroke-width="1.8" fill="none"/></svg></span></a>
</section>

<footer>
  <svg class="footer-band" viewBox="0 0 1200 564">
    <path d="M0 130 C240 0 700 -10 1200 80 L1200 564 L0 564 Z" fill="#1d5c9b"/>
    <path d="M0 146 C250 18 700 10 1200 96 L1200 564 L0 564 Z" fill="#141414"/>
  </svg>
  <div class="footer-brand"><i></i>Quiet Path</div>
  <div class="footer-col" style="left:449px"><h3>Quick Links</h3><ul><li>Home</li><li>About Us</li><li>Vision Statement</li><li>People</li><li>Projects</li><li>FAQs</li></ul></div>
  <div class="footer-col" style="left:634px"><h3>Legal</h3><ul><li>Copyright</li><li>Legal</li><li>Privacy</li><li>Accessibility</li><li>Sitemap</li></ul></div>
  <div class="footer-col" style="left:768px"><h3>Contact Us</h3></div>
  <div class="contact-row" style="top:4344px"><svg width="16" height="22" viewBox="0 0 16 22"><path d="M8 0a8 8 0 0 1 8 8c0 6-8 14-8 14S0 14 0 8a8 8 0 0 1 8-8z" fill="#57a843"/><circle cx="8" cy="8" r="3" fill="#141414"/></svg><span>2280 Larkspur Lane, Fenwick,<br>Ohio, USA. 40913</span></div>
  <div class="contact-row" style="top:4403px"><svg width="18" height="18" viewBox="0 0 14 14"><path d="M3 1l2.5 3-1.5 2c1 2 2 3 4 4l2-1.5 3 2.5-1.5 2.5C6 13 1 8 .5 3z" fill="#57a843"/></svg><span>Phone Number<br>555 010 4821</span></div>
  <div class="contact-row" style="top:4461px"><svg width="20" height="15" viewBox="0 0 14 11"><rect width="14" height="11" rx="1" fill="#57a843"/><path d="M1 1l6 5 6-5" stroke="#141414" stroke-width="1.3" fill="none"/></svg><span>Email<br>hello@quietpath.example</span></div>
  <div class="to-top"><svg width="14" height="14" viewBox="0 0 14 14"><path d="M2 9l5-5 5 5" stroke="#141414" stroke-width="2" fill="none"/></svg></div>
  <div class="footer-rule"></div>
  <p class="copyright">Copyrights ©2021. All Rights Reserved</p>
  <nav class="legal-links"><a href="#">Privacy Policy</a><span>|</span><a href="#">Site Map</a></nav>
</footer>

</body>
</html>
```